Northern Summit Builders & Affiliates Redesigning our Look

We need stationary (letterhead, envelopes, notepads, invoicing templates, etc) that all coordinate. We are an commerial and residential exteriors construction company that operates 3 companies which all run exclusively, however, the compliment one another well.

Northern Summit Builders (this company installs exteriors on jobsites both residential and commercial)
Northern Summit Roofing & Building Supply (this company sells exterior building materials to homeowners and builders.)
Northern Summit Dumpster Services (This company delivers roll away dumpster cans to homeowners and builders)

Just a note: When I say we do exterior work. We do roofing, siding, stone, windows/doors, gutters, and decks.

We are looking for stationary that includes all three and keeps with our patriotic theme

Info on our firm:
Address: 2718 Tamarind Rd, Elkton MI 48512
Phone: 231-555-0172
Website: www.northernsummit-example.us

Target Market(s)

Our companies target market is vast. We work in the B2B space as well as with homeowner (retail customers). We are in the home and commercial buiding construction field. We specialized in exteriors. (Roofing, Siding, Stone, Windows, Doors, Decks, Gutters)

Industry/Entity Type

Construction

Colors
ec1f27
ffffff
0555a3

Requirements
Must have
• Would like to have a clean professional look with a patriotic theme
Nice to have
• Red/White/Blue

```html
<!DOCTYPE html>
<html lang="en">
<head>
<meta charset="utf-8">
<title>Northern Summit Dumpster Services – Letterhead</title>
<link href="https://fonts.googleapis.com/css2?family=Cabin:wght@500&family=Arimo&family=Roboto+Condensed:wght@700&display=swap" rel="stylesheet">
<style>
  :root {
    --brand-red: #ec1f27;
    --brand-blue: #0555a3;
    --paper: #ffffff;
    --ink: #111111;
    --band-top: #c9cde0;
    --wash-blue: #d9dbe6;
    --wash-red: #f6d3d4;
  }
  * { margin: 0; padding: 0; box-sizing: border-box; }
  html, body { width: 927px; height: 1200px; overflow: hidden; background: var(--paper); }
  .letterhead {
    position: relative;
    width: 927px;
    height: 1200px;
    background: var(--paper);
    overflow: hidden;
    font-family: "Cabin", sans-serif;
    color: var(--ink);
  }
  .top-band {
    position: absolute;
    left: 0; top: 0;
    width: 100%; height: 56px;
    background: linear-gradient(to bottom, var(--band-top), rgba(255,255,255,0));
  }
  .brand {
    position: absolute;
    left: 76px; top: 78px;
    display: flex;
    align-items: center;
    gap: 10px;
  }
  .brand-square {
    width: 26px; height: 26px;
    background: var(--brand-blue);
  }
  .brand-name {
    font-family: "Cabin", sans-serif;
    font-weight: 500;
    font-size: 20px;
    line-height: 1.15;
    color: var(--ink);
    width: 190px;
  }
  .background-wash {
    position: absolute;
    left: 12px; top: 366px;
    width: 915px; height: 560px;
    border-radius: 60px 0 0 120px;
    background: linear-gradient(100deg, var(--wash-blue) 0%, var(--wash-blue) 35%, var(--wash-red) 48%, rgba(246,211,212,0.5) 100%);
    opacity: 0.75;
  }
  .date {
    position: absolute;
    left: 108px; top: 238px;
    font-family: "Arimo", sans-serif;
    font-size: 13px;
  }
  .letter-body {
    position: absolute;
    left: 108px; top: 366px;
    width: 710px;
    font-size: 13.4px;
    line-height: 18.2px;
  }
  .salutation { margin-bottom: 18px; }
  .letter-body p.paragraph { margin-bottom: 18px; hyphens: auto; }
  .closing { margin-top: 34px; }
  .footer-contact {
    position: absolute;
    left: 0; top: 1168px;
    width: 100%;
    display: flex;
    justify-content: center;
    gap: 64px;
    font-family: "Roboto Condensed", sans-serif;
    font-weight: 700;
    font-size: 11px;
    letter-spacing: 1.8px;
    color: var(--ink);
  }
</style>
</head>
<body>
<div class="letterhead">
  <div class="top-band"></div>

  <div class="brand">
    <span class="brand-square"></span>
    <span class="brand-name">Northern Summit Dumpster Services</span>
  </div>

  <div class="background-wash" role="img" aria-label="Faint brushed red, white and blue banner behind the letter text"></div>

  <div class="date">01-02-2017</div>

  <div class="letter-body">
    <p class="salutation">Dear Client,</p>
    <p class="paragraph">Alitatis volenie nectem aut pla que eicae el est autem et proribus, quunderspe nus volor accatium eic tet lant aribeat uritem alictibus, experi velecul lignit et eum vere pa natet laccus nam, nullab iur, conet fugia simaxim oluptatius, id eariorectae. Adia dolum vel ipsanto cus doluptati dolorpor resto to erum vel inissitium non parum iur? Qui demquae libus, od molorem acit magnati consecto mi, temporem et aliquas unt voluptatur aut officia autatis perferitius as aut velignis et parisqui ut as et, niet imolorem repuditate cus is magni aspernatem hillat harum quae molo est aligenimust voloratus reperepe quis ma conseque inciisciis reseque ea ne consecepero ium ipideli gentibu sciet, num fuga. On pelit experum, nonsectint, sus dolorae prorro cum ligenim oluptae dolupti busciametur? Os simpero di nos nis ex et lam con perferum ut repe aut a ius desersped quid es expellam doluptate nos aut am, offictotame am fuga.</p>
    <p class="paragraph">Natis quo quisit, cor solorae parchillest molupta tessita net, consendit, acerrup taspera eculpa pro eos quamet odi ditiusandam quidellupita consequis aliquasim etur, qui te volenisci doluptin corum et et utem consequi adi berumquod magniendelit volore culpa qui sitasse rchiciunt, cum facculpa quides voluptios duciist inctiis reheniae natendit re volores tiatquis debis dolupta tumenempores secta sincimusam am ea quam faccum as mo vendit, aut mi, officitat pro offic te nectia doloruptate eium eatiumquid exernatem quam estiate voles explit lam ipsumqui ut essi doloreh enduntiandi venditam as quae aut acidusda dolore se minctiae et renditatecea il illant es accaest, susandit pedit velit molorem.</p>
    <p class="paragraph">Itaquam usciliq uisqui volorpor maximagnim inis aute re dus qui nihicit as porro berrum eaquam imi, untio. Et et quoditae voluptate nis at prendis et est aligent ium endebitam re num essedi sae verum ipsam autenihil miliquatur maio. Cia nis modit, ut quunt volent uta quametur remporpost od ut abor adignih itatius dolo volo dolo ex expe voloreiur sapellitat assum ad esequod issequi blaturistrum reriaer feriaest acid quas ma dolliciis eos doluptustis ducite adiat.</p>
    <p class="closing">Sincerely,</p>
  </div>

  <div class="footer-contact">
    <span class="footer-address">2718 Tamarind Rd.&nbsp;&nbsp;&nbsp;Elkton, MI&nbsp;&nbsp;48512</span>
    <span class="footer-phone">T:231.555.0172</span>
    <span class="footer-web">www.NorthernSummit-example.us</span>
  </div>
</div>
</body>
</html>
```